LED panel tester - hand-held test tool - simple label required

I have designed a product to test the LED panels of a road-side variable message sign (VMS). I don't expect to sell too many of these but thought it would look professional if it had a proper label.

I need a label designed for this hand-held test equipment. Attached is the positional layout of all the switches and text. I have also included a photo of the product.

A simple Google image search of "hand-held test tool" shows that it doesn't have to be fancy but rather functional.

I would like to put branding on the bottom 1/5th and have the option to interchange the brand if I ever get approached by one of the manufacturers of these signs. Initially it will just have a link to my website (BrightKettleWorks.com.au) right down at the bottom.

```html
<!DOCTYPE html>
<html lang="en">
<head>
<meta charset="utf-8">
<title>VMS Panel Tester Label</title>
<link rel="stylesheet" href="https://fonts.googleapis.com/css2?family=Arimo:wght@400;700&display=swap">
<style>
  :root {
    --brand-blue: #0b63b8;
    --label-white: #efeff0;
    --trace-grey: #d9d9db;
    --ink: #111111;
    --cutout: #1b1c1e;
    --page: #e4e3de;
  }
  html, body {
    margin: 0;
    padding: 0;
    width: 729px;
    height: 1200px;
    overflow: hidden;
    background: var(--page);
    font-family: "Arimo", Arial, sans-serif;
  }
  .label {
    position: absolute;
    left: 102px;
    top: 20px;
    width: 525px;
    height: 1160px;
    background: var(--label-white);
    overflow: hidden;
  }
  .trace-pattern {
    position: absolute;
    left: 0;
    top: 76px;
    width: 525px;
    height: 1024px;
    background: linear-gradient(180deg, var(--label-white) 0%, var(--label-white) 45%, var(--trace-grey) 100%);
  }
  .header-band {
    position: absolute;
    left: 0;
    top: 0;
    width: 100%;
    height: 76px;
    background: var(--brand-blue);
    color: #ffffff;
    font-weight: 700;
    font-size: 39px;
    line-height: 76px;
    text-align: center;
    letter-spacing: 0.5px;
  }
  .switch-ring {
    position: absolute;
    width: 44px;
    height: 44px;
    margin: -27px 0 0 -27px;
    border: 5px solid var(--brand-blue);
    border-radius: 50%;
    background: var(--cutout);
  }
  .switch-label {
    position: absolute;
    font-weight: 700;
    font-size: 31px;
    line-height: 1;
    color: var(--ink);
    transform: translateY(-50%);
  }
  .switch-label.left { text-align: right; }
  .rocker-frame {
    position: absolute;
    left: 143px;
    top: 674px;
    width: 215px;
    height: 143px;
    border: 11px solid var(--brand-blue);
    background: var(--cutout);
  }
  .power-led {
    position: absolute;
    left: 436px;
    top: 709px;
    width: 32px;
    height: 32px;
    margin: -21px 0 0 -21px;
    border: 5px solid var(--brand-blue);
    border-radius: 50%;
    background: #5a7a2c;
  }
  .power-label {
    position: absolute;
    left: 389px;
    top: 750px;
    font-weight: 700;
    font-size: 31px;
    line-height: 1;
    color: var(--ink);
  }
  .footer-band {
    position: absolute;
    left: 0;
    top: 1100px;
    width: 100%;
    height: 60px;
    background: var(--brand-blue);
    color: #ffffff;
    font-size: 30px;
    line-height: 60px;
    text-align: center;
    font-weight: 400;
  }
</style>
</head>
<body>
  <div class="label">
    <div class="trace-pattern" role="img" aria-label="Light grey circuit-board trace pattern running behind the controls"></div>

    <div class="header-band">VMS PANEL TESTER</div>

    <div class="switch-ring" style="left:262px;top:210px"></div>
    <div class="switch-label" style="left:340px;top:212px">RED</div>

    <div class="switch-ring" style="left:259px;top:293px"></div>
    <div class="switch-label" style="left:340px;top:292px">GREEN</div>

    <div class="switch-ring" style="left:260px;top:368px"></div>
    <div class="switch-label" style="left:340px;top:370px">ORANGE</div>

    <div class="switch-ring" style="left:259px;top:446px"></div>
    <div class="switch-label" style="left:340px;top:447px">WHITE</div>

    <div class="switch-ring" style="left:259px;top:527px"></div>
    <div class="switch-label" style="left:339px;top:528px">BLUE</div>

    <div class="switch-ring" style="left:260px;top:602px"></div>
    <div class="switch-label left" style="right:346px;top:606px">FAST</div>
    <div class="switch-label" style="left:339px;top:606px">SLOW</div>

    <div class="rocker-frame"></div>

    <div class="power-led"></div>
    <div class="power-label">POWER</div>

    <div class="footer-band">www.BrightKettleWorks.com.au</div>
  </div>
</body>
</html>
```